Events floral designer business needs a logo design

I need a logo design for my floral design business called tender thistles.
i am inspired by nature and the simplicity of its beauty, whilst upcycling and recycling materials to reduce waste and impact on our environment.
I would like the design to be printed on recycled brown cardboard so i would like a simple but striking design of a bold black ivy vine or gnarly magnolia or tree branch with lower case old school type writer font.

Target Market(s)

Anyone requiring floral additions for their event

Industry/Entity Type

Business

Contact Information for Business Card

rosa kettering
floral designer/creator
0461807352
rosa@tenderthistles.com
tenderthistles.com

Font styles to use
Other font styles liked:
• lower case type writer

Colors
000000

Requirements
Must have
• simplicity but boldness
• Black typewriter font and bold picture with my details
Nice to have
• as above
Should not have
• colour

```html
<!DOCTYPE html>
<html lang="en">
<head>
<meta charset="utf-8">
<title>Tender Thistles – Business Card</title>
<link rel="stylesheet" href="https://fonts.googleapis.com/css2?family=Montserrat:wght@300;400;500;700&display=swap">
<style>
  :root {
    --stage-light: #ffffff;
    --stage-dark: #a9a9a9;
    --card-light: #e9e9e9;
    --card-dark: #c4c4c4;
    --band-edge: #050505;
    --band-mid: #2a2a2a;
    --band-rim: #f4f4f4;
    --ink: #1d1d1d;
    --label: #3a3a3a;
    --on-band: #ffffff;
    --divider: #8a8a8a;
  }
  * { margin: 0; padding: 0; box-sizing: border-box; }
  html, body { width: 1200px; height: 1200px; overflow: hidden; }
  body {
    position: relative;
    font-family: "Montserrat", sans-serif;
    background: radial-gradient(ellipse 60% 60% at 50% 48%, var(--stage-light) 0%, #e6e6e6 55%, var(--stage-dark) 100%);
  }
  .card {
    position: absolute;
    border-radius: 16px;
    background: radial-gradient(ellipse at 45% 35%, var(--card-light) 0%, #d8d8d8 60%, var(--card-dark) 100%);
    box-shadow: 0 1px 2px rgba(0,0,0,0.08);
  }
  .card--front { left: 208px; top: 94px; width: 838px; height: 480px; }
  .card--back { left: 204px; top: 630px; width: 836px; height: 478px; }

  .band {
    position: absolute;
    border: 3px solid var(--band-rim);
    border-bottom: none;
    border-radius: 24px 24px 0 0;
    background: radial-gradient(ellipse 55% 110% at 50% 10%, var(--band-mid) 0%, #111 60%, var(--band-edge) 100%);
    color: var(--on-band);
  }
  .card--front .band { left: 28px; right: 28px; bottom: 0; height: 116px; }
  .card--back .band { left: -7px; right: -4px; bottom: 0; height: 174px; }

  .brand {
    position: absolute;
    display: flex;
    align-items: center;
    gap: 12px;
    transform: translate(-50%, -50%);
    color: var(--ink);
    font-weight: 500;
    font-size: 30px;
    white-space: nowrap;
  }
  .brand__dot {
    width: 22px; height: 22px;
    border-radius: 50%;
    border: 3px solid var(--ink);
  }
  .card--front .brand { left: 410px; top: 234px; }
  .card--back .brand { left: 416px; top: 162px; }

  .web {
    position: absolute; left: 0; right: 0; top: 44px;
    text-align: center;
    font-weight: 300;
    font-size: 35px;
    letter-spacing: 1px;
  }

  .contact-name {
    position: absolute; left: 44px; top: 52px;
    font-weight: 700; font-size: 33px; letter-spacing: 1px;
    white-space: nowrap;
  }
  .contact-role {
    position: absolute; left: 46px; top: 112px;
    font-weight: 500; font-size: 20px;
    white-space: nowrap;
  }
  .contact-divider {
    position: absolute; left: 426px; top: 56px;
    width: 2px; height: 74px; background: var(--divider);
  }
  .contact-phone {
    position: absolute; left: 488px; top: 44px;
    font-weight: 700; font-size: 46px; letter-spacing: 1px;
    white-space: nowrap;
  }
  .contact-email {
    position: absolute; left: 490px; top: 106px;
    font-weight: 300; font-size: 24px; letter-spacing: 0.5px;
    white-space: nowrap;
  }

  .side-label {
    position: absolute; left: 0; right: 0;
    text-align: center;
    color: var(--label);
    font-weight: 400; font-size: 26px; letter-spacing: 1px;
  }
  .side-label--front { top: 586px; left: 26px; }
  .side-label--back { top: 1133px; left: 14px; }
</style>
</head>
<body>
  <section class="card card--front">
    <div class="brand"><span class="brand__dot"></span><span>tender thistles</span></div>
    <div class="band">
      <p class="web">www.tenderthistles.com</p>
    </div>
  </section>
  <p class="side-label side-label--front">FRONT</p>

  <section class="card card--back">
    <div class="brand"><span class="brand__dot"></span><span>tender thistles</span></div>
    <div class="band">
      <p class="contact-name">ROSA KETTERING</p>
      <p class="contact-role">FLORAL DESIGNER/ CREATOR</p>
      <span class="contact-divider"></span>
      <p class="contact-phone">0461807352</p>
      <p class="contact-email">rosa@tenderthistles.com</p>
    </div>
  </section>
  <p class="side-label side-label--back">BACK</p>
</body>
</html>
```